Vex

I have the logo for the back already. Need the front to match.
Need a VEX logo which I can provide or you can download one - VEX Realty in canada... Back of the card will be my logo and name. Front will have the info...
I would like a black background. Match colors on front to the back..
Details on Card

Target Market(s)

Realestate clients.. Keep it classy like the logo

Contact Information for Business Card

Moren Tadwick office - 5817730264 cell - 5819063147 email - Moren@MorenTadwick.Com. website - MorenTadwick.Com Facebook - MTadwRealty Instagram - Moren_Qpl_Realtor Address - 418 - 23 St NE | K5P2M8

Colors
3176b5
33a6d7
85cae6

Requirements
Must have
• same color scheme as the logo
logo will be on the back
Black Background
Horizontal card
The one side of the card should be clean. like I stated, just my logo " Moren Tadwick " and nothing else

```html
<!DOCTYPE html>
<html lang="en">
<head>
<meta charset="utf-8">
<title>Moren Tadwick – Business Card</title>
<link rel="stylesheet" href="https://fonts.googleapis.com/css2?family=Lato:wght@400;700&display=swap">
<style>
  :root {
    --backdrop: #2b2b2d;
    --card-top: #222224;
    --card-bottom: #161617;
    --brand-blue: #3176b5;
    --brand-blue-bright: #1f7fd0;
    --text-light: #f2f2f2;
    --icon-blue: #2f86cf;
    --pin-red: #e0242f;
    --social-dot: #3b5aa8;
    --social-dot-alt: #d9456a;
  }
  * { margin: 0; padding: 0; box-sizing: border-box; }
  html, body {
    width: 1200px; height: 900px; overflow: hidden;
    background: var(--backdrop);
    font-family: "Lato", Arial, sans-serif;
  }
  .canvas {
    width: 1200px; height: 900px;
    display: flex; flex-direction: column; align-items: center; justify-content: center;
    gap: 32px;
  }
  .card {
    position: relative;
    width: 720px; height: 411px;
    border-radius: 26px;
    background: radial-gradient(ellipse at 50% 40%, var(--card-top), var(--card-bottom) 80%);
    box-shadow: 0 18px 40px rgba(0,0,0,0.55);
    color: var(--text-light);
    overflow: hidden;
  }

  /* Front */
  .name-pill {
    position: absolute; left: 34px; top: 38px;
    background: var(--brand-blue-bright);
    color: #fff;
    font-weight: 700; font-size: 21px; letter-spacing: 1px;
    padding: 9px 26px; border-radius: 22px;
  }
  .contact-list {
    position: absolute; left: 64px; top: 110px;
    list-style: none;
  }
  .contact-list li {
    display: flex; align-items: center; gap: 14px;
    font-size: 20px; line-height: 32px; letter-spacing: 0.5px;
  }
  .contact-list .label { font-weight: 700; }
  .contact-list svg { width: 20px; height: 20px; flex: none; }
  .wordmark {
    position: absolute; right: 50px; top: 62px;
    color: var(--brand-blue-bright);
    font-weight: 400; font-size: 38px; letter-spacing: 4px;
    text-transform: uppercase;
    text-align: right;
    line-height: 1.15;
  }
  .address {
    position: absolute; right: 48px; top: 216px;
    display: flex; align-items: center; gap: 10px;
    font-size: 19px; letter-spacing: 0.5px;
  }
  .address svg { width: 18px; height: 22px; }
  .social-row {
    position: absolute; left: 64px; bottom: 40px;
    display: flex; gap: 52px;
  }
  .social-item {
    display: flex; align-items: center; gap: 12px;
    font-size: 20px; letter-spacing: 0.5px;
  }
  .social-dot { width: 20px; height: 20px; border-radius: 50%; background: var(--social-dot); }
  .social-dot.alt { background: var(--social-dot-alt); }

  /* Back */
  .card-back { display: flex; align-items: center; justify-content: center; }
  .card-back .wordmark {
    position: static;
    font-size: 54px; letter-spacing: 6px; text-align: center;
  }
</style>
</head>
<body>
<main class="canvas">
  <section class="card card-front" aria-label="Card front">
    <div class="name-pill">MOREN TADWICK</div>
    <ul class="contact-list">
      <li>
        <svg viewBox="0 0 24 24" fill="var(--icon-blue)"><path d="M3 9c0-3 4-5 9-5s9 2 9 5v2h-5V9c-1-.6-2.4-1-4-1s-3 .4-4 1v2H3z"/><rect x="5" y="13" width="14" height="8" rx="2"/></svg>
        <span>5817730264 <span class="label">(office)</span></span>
      </li>
      <li>
        <svg viewBox="0 0 24 24" fill="none" stroke="var(--icon-blue)" stroke-width="2"><rect x="6" y="2" width="12" height="20" rx="2"/><line x1="10" y1="18" x2="14" y2="18"/></svg>
        <span>5819063147</span>
      </li>
      <li>
        <svg viewBox="0 0 24 24" fill="var(--icon-blue)"><path d="M2 5h20v14H2z"/><path d="M2 5l10 8 10-8" fill="none" stroke="#161617" stroke-width="1.8"/></svg>
        <span>Moren@MorenTadwick.Com.</span>
      </li>
      <li>
        <svg viewBox="0 0 24 24" fill="none" stroke="var(--icon-blue)" stroke-width="1.8"><circle cx="12" cy="12" r="10"/><ellipse cx="12" cy="12" rx="4.5" ry="10"/><line x1="2" y1="12" x2="22" y2="12"/></svg>
        <span>MorenTadwick.Com</span>
      </li>
    </ul>
    <div class="wordmark">Moren<br>Tadwick</div>
    <div class="address">
      <svg viewBox="0 0 18 22"><path d="M9 0a8 8 0 0 0-8 8c0 6 8 14 8 14s8-8 8-14a8 8 0 0 0-8-8z" fill="var(--pin-red)"/><circle cx="9" cy="8" r="3" fill="#fff"/></svg>
      <span>418 - 23 St NE | K5P2M8</span>
    </div>
    <div class="social-row">
      <div class="social-item"><span class="social-dot"></span><span>MTadwRealty</span></div>
      <div class="social-item"><span class="social-dot alt"></span><span>Moren_Qpl_Realtor</span></div>
    </div>
  </section>

  <section class="card card-back" aria-label="Card back">
    <div class="wordmark">Moren Tadwick</div>
  </section>
</main>
</body>
</html>
```